Brantmoor Financial Coaching LLC - Needed clean black business card

Business card for personal financial coaching practice located on Las Vegas NV, new startup. Back of card needs to have "how it works" to match the website.

Font styles to use
Sans Serif

Colors

Designer to choose colors to be used in the design.

```html
<!DOCTYPE html>
<html lang="en">
<head>
<meta charset="utf-8">
<title>Brantmoor Financial Coaching LLC – Business Card</title>
<link rel="stylesheet" href="https://fonts.googleapis.com/css2?family=Questrial&display=swap">
<style>
  :root {
    --backdrop: #1e1e1f;
    --card: #0f0f10;
    --ink: #f4f4f4;
    --icon: #9a9a9a;
    --rule: #d8d8d8;
  }
  * { margin: 0; padding: 0; box-sizing: border-box; }
  html, body {
    width: 1200px;
    height: 1200px;
    overflow: hidden;
    background: var(--backdrop);
  }
  body {
    font-family: "Questrial", "Century Gothic", sans-serif;
    color: var(--ink);
    position: relative;
  }
  .card {
    position: absolute;
    left: 150px;
    width: 900px;
    height: 514px;
    background: var(--card);
    box-shadow: 0 18px 40px rgba(0,0,0,0.55);
  }
  .card--back { top: 62px; }
  .card--front { top: 624px; }

  /* Back */
  .how-it-works {
    position: absolute;
    left: 120px;
    top: 120px;
    right: 60px;
  }
  .how-it-works h2 {
    font-size: 24px;
    font-weight: 700;
    letter-spacing: 0.3px;
    margin-bottom: 10px;
  }
  .how-it-works ul {
    list-style: none;
  }
  .how-it-works li {
    position: relative;
    font-size: 19px;
    line-height: 33px;
    padding-left: 28px;
    letter-spacing: 0.2px;
  }
  .how-it-works li::before {
    content: "";
    position: absolute;
    left: 0;
    top: 12px;
    width: 9px;
    height: 9px;
    border-radius: 50%;
    background: var(--ink);
  }

  /* Front */
  .company-name {
    position: absolute;
    right: 60px;
    top: 108px;
    font-size: 30px;
    font-weight: 400;
    letter-spacing: 1.5px;
    text-transform: uppercase;
  }
  .person-name {
    position: absolute;
    left: 80px;
    top: 258px;
    font-size: 28px;
    letter-spacing: 0.5px;
  }
  .rule {
    position: absolute;
    left: 70px;
    right: 70px;
    top: 302px;
    height: 2px;
    background: var(--rule);
  }
  .contact-list {
    position: absolute;
    left: 70px;
    top: 318px;
    list-style: none;
  }
  .contact-list li {
    display: flex;
    align-items: center;
    gap: 14px;
    font-size: 24px;
    line-height: 36px;
  }
  .contact-list svg {
    width: 22px;
    height: 22px;
    flex: none;
    fill: none;
    stroke: var(--icon);
    stroke-width: 1.8;
  }
  .contact-list svg.solid { fill: var(--icon); stroke: none; }
  .address {
    position: absolute;
    right: 70px;
    top: 330px;
    text-align: right;
    font-size: 24px;
    line-height: 36px;
    letter-spacing: 0.5px;
    font-style: normal;
  }
</style>
</head>
<body>

<section class="card card--back">
  <div class="how-it-works">
    <h2>How It Works</h2>
    <ul>
      <li>All free one-time consultations are in-person meetings only.</li>
      <li>Paid appointments may be scheduled for in-person or virtual meetings.</li>
      <li>Select the session, date and time that works best for your schedule.</li>
      <li>Start your journey of financial freedom at brantmoorfinancialcoaching.com</li>
    </ul>
  </div>
</section>

<section class="card card--front">
  <h1 class="company-name">Brantmoor Financial Coaching LLC</h1>
  <p class="person-name">Dorian Hale</p>
  <div class="rule"></div>
  <ul class="contact-list">
    <li>
      <svg class="solid" viewBox="0 0 24 24" aria-hidden="true"><path d="M6.6 10.8a15.1 15.1 0 0 0 6.6 6.6l2.2-2.2a1 1 0 0 1 1-.25 11.4 11.4 0 0 0 3.6.57 1 1 0 0 1 1 1V20a1 1 0 0 1-1 1A17 17 0 0 1 3 4a1 1 0 0 1 1-1h3.5a1 1 0 0 1 1 1c0 1.25.2 2.45.57 3.57a1 1 0 0 1-.25 1z"/></svg>
      702-555-0148
    </li>
    <li>
      <svg viewBox="0 0 24 24" aria-hidden="true"><rect x="2.5" y="5" width="19" height="14"/><path d="M2.5 5l9.5 8 9.5-8"/></svg>
      Dorian@brantmoorfinancialcoaching.com
    </li>
    <li>
      <svg viewBox="0 0 24 24" aria-hidden="true"><circle cx="12" cy="12" r="9.5"/><ellipse cx="12" cy="12" rx="4.2" ry="9.5"/><path d="M2.5 12h19M4 7h16M4 17h16"/></svg>
      brantmoorfinancialcoaching.com
    </li>
  </ul>
  <address class="address">4120 W Sahara Ave #305-B<br>Las Vegas, NV 89102</address>
</section>

</body>
</html>
```